Swimming Pool Service Website needed!!!

Hi Everyone! Thanks for looking at my contest. I PROMISE to provide excellent feedback during this process.

I am starting a new swimming pool business cleaning company in San Diego, California and would like your help in making it similar to one of these two websites that are already functioning.

http://www.brightmeadowhub.example/services-repair.html

http://tryvelmarktide.example/commercial-pool-cleaning.php

I like these two because they are easy to read, classy, sophisticated and have nice pictures of really clean & clear pools.

I really like the blue on white color format.

I do not have a logo, but the name of my company is HARBORLINE POOL SERVICE.

My tag line is: Water so bright, you'll want to dive right in. (does not need to have the quotes around "in"...maybe just italics for this word IN?) You decide for me.

I would like to have a logo designed that incorporates some sort of easy to read letters. I do not want cursive (handwriting) letters. I thought about having a "reflection" of letters (mirror image), but think that this will be hard to read from far away. Maybe you can surprise me and come up with an idea that works using the a mirror image....but I'm not sure. I was leaning toward plain old BLOCK letters as I think it would be easy to read on my truck.

I would like to have 5 pages on my website:
1) Home
2) About Us (Know Your Poolman) / Why Hire Us
3) Services Offered
4) FAQ's
5) Contact

I am looking for a fully-functioning website (coded). Upon selection of the design winner, I am offering to increase the budget/payment by $100-$125 for the coding of all the pages. So anyone looking at participating in this contest, should be willing and able to provide the coding to the webpages that i've requested.

Target Market(s)

Upper middle-class homeowners who have a pool

Industry/Entity Type

Pool Service

Number of Pages Required

5+ page

Font styles to use
Serif

Colors
0455a3
3276b5
85acd3
85cae6
ffffff
33a6d7
0592cd

Requirements
Must have
• The Home page must have this picture highlighted in the top of the page:
• http://www.dunecrestwaterman.example/
• Must have pictures of some high-end pools. Any that you can find on the internet are wonderful.
• Must have a table on the right of the home page that mentions the service areas that we go to:
• • Carmel Valley (92130)
• • Del Mar (92014)
• • Rancho Santa Fe (92067)
• • Solana Beach (92075)
• • Santaluz (92127)
• • Cardiff (92007)
• • Encinitas (92024)
• • Carlsbad (92009, 92008)
• • La Jolla (92037)
• • Pacific Beach (92109)
• • Mira Mesa (92126)
• • Sorrento Valley (92121)
• • Clairemont (92117)
• • Rancho Bernardo (92127, 92128)
• • Rancho Penasquitos (92129)
• • Poway (92064)
Nice to have
• Maybe incorporate some pictures of some kids (or families) playing in pools on the Why Hire Us page?
• I also like the feel of this website, but posting this page just for reference so you can get a feel more of what I like:
• http://www.ferrovaletide.example/
• I like the FAQ's page from this website. I like how you can click on the question and then it pops up with the answer. http://www.quillbrookaquacare.example/pool-spa-fountain-faqs/

```html
<!DOCTYPE html>
<html lang="en">
<head>
<meta charset="utf-8">
<title>Harborline Pool Service</title>
<link rel="stylesheet" href="https://fonts.googleapis.com/css2?family=Raleway:wght@300;400;600&family=Open+Sans:ital,wght@0,400;0,600;1,400&display=swap">
<style>
:root{
  --navy:#0455a3;
  --mid:#3276b5;
  --soft:#85acd3;
  --sky:#85cae6;
  --bright:#33a6d7;
  --azure:#0592cd;
  --white:#ffffff;
  --ink:#3b3b3b;
  --night:#1a1a1a;
  --line:#9fcbe6;
}
*{box-sizing:border-box;margin:0;padding:0}
html,body{width:1200px;height:4358px;overflow:hidden}
body{position:relative;background:var(--white);font-family:"Open Sans",Arial,sans-serif;color:var(--ink)}
.abs{position:absolute}

/* header */
.site-header{left:0;top:0;width:1200px;height:100px;background:var(--white);z-index:3}
.brand{left:94px;top:14px;color:var(--azure);font-family:"Raleway",Arial,sans-serif;font-weight:600;line-height:1}
.brand .name{font-size:40px;letter-spacing:1px;display:block}
.brand .sub{font-size:19px;letter-spacing:5px;display:block;margin-top:4px;padding-left:2px}
.nav{right:94px;top:26px;display:flex;list-style:none}
.nav li{font-size:13px;color:#555;padding:8px 12px;letter-spacing:.5px;text-transform:uppercase}
.nav li.active{background:#eaeaea;color:#333;font-weight:600}
.dropdown{left:694px;top:108px;width:184px;background:#1e1e1e;z-index:4;list-style:none;padding:10px 0}
.dropdown li{color:var(--white);font-size:11px;font-weight:600;padding:8px 16px;text-transform:uppercase}
.dropdown li.current{color:var(--sky)}

/* hero */
.hero{left:0;top:100px;width:1200px;height:489px;background:linear-gradient(180deg,#cfe9f6 0%,var(--sky) 60%,#6fc0e2 100%);overflow:hidden}
.hero-band{left:0;top:0;width:1200px;height:36px;background:var(--bright)}
.hero-band-thin{left:0;top:36px;width:1200px;height:8px;background:var(--azure);opacity:.5}
.hero-photo{left:141px;top:61px;width:918px;height:335px;background:linear-gradient(160deg,#bfe6f7 0%,var(--bright) 45%,var(--azure) 100%);border:6px solid var(--white)}
.tagline{left:0;top:412px;width:1200px;text-align:center;color:var(--white);font-family:"Raleway",Arial,sans-serif;font-weight:600;font-size:24px}
.tagline em{font-style:italic}

/* intro */
.intro-title{left:94px;top:636px;width:1012px;text-align:center;color:var(--azure);font-family:"Raleway",Arial,sans-serif;font-size:26px;font-weight:400;line-height:1.4}
.intro-photo{left:94px;top:731px;width:493px;height:248px;background:linear-gradient(135deg,#d8eff9,var(--sky) 60%,var(--bright))}
.intro-copy{left:613px;top:741px;width:493px;font-size:14px;line-height:1.6;color:#555}
.intro-copy p{margin-bottom:14px}
.intro-copy a{color:var(--azure);text-decoration:none}

/* projects */
.projects{left:0;top:1046px;width:1200px;height:871px;background:linear-gradient(180deg,var(--bright),#5db6e0 50%,var(--bright))}
.section-title{font-family:"Raleway",Arial,sans-serif;font-weight:300;font-size:40px;text-align:center}
.projects .section-title{position:absolute;left:0;top:32px;width:1200px;color:var(--white)}
.project-grid{left:94px;top:117px;width:1012px;height:674px;display:grid;grid-template-columns:repeat(3,1fr);grid-template-rows:repeat(2,1fr);gap:4px}
.tile{position:relative}
.tile.t1{background:#1d2a33}
.tile.t2{background:linear-gradient(180deg,#8b6a8a,#3fa7c4)}
.tile.t3{background:linear-gradient(180deg,#b9c6cc,#4fa3c0)}
.tile.t4{background:linear-gradient(180deg,#5fb5e8,#1a86c9)}
.tile.t5{background:linear-gradient(180deg,#37505e,#2bbfd0)}
.tile.t6{background:linear-gradient(180deg,#9c6b3c,#41b2d4)}
.tile-label{position:absolute;left:0;top:148px;width:100%;text-align:center;color:var(--white);font-family:"Raleway",Arial,sans-serif;font-size:20px}
.tile-plus{position:absolute;right:0;top:0;width:34px;height:34px;background:var(--bright);color:var(--white);text-align:center;line-height:34px;font-size:22px}

/* services */
.services-title{left:94px;top:1956px;width:640px;color:var(--azure)}
.service-list{top:2060px;width:300px;list-style:none}
.service-list li{position:relative;height:100px;padding-left:50px;font-size:18px;line-height:1.4;color:var(--azure)}
.service-list svg{position:absolute;left:0;top:4px}
.col-a{left:94px}
.col-b{left:446px}
.areas-title{left:788px;top:1956px;width:320px;text-align:left;color:var(--azure)}
.area-list{left:788px;top:2058px;width:318px;list-style:none}
.area-list li{height:45px;border:1px solid var(--line);margin-bottom:11px;padding:0 10px;line-height:43px;font-size:15px;color:var(--azure)}

/* testimonial */
.testimonials{left:0;top:3141px;width:1200px;height:379px;background:linear-gradient(180deg,var(--bright),#4db1dd)}
.testimonials .section-title{position:absolute;left:0;top:60px;width:1200px;color:var(--white)}
.quote{left:200px;top:150px;width:800px;text-align:center;color:var(--white);font-style:italic;font-size:17px;line-height:1.65}
.quote strong{font-weight:600}
.cite{left:0;top:252px;width:1200px;text-align:center;color:var(--white);font-size:13px;letter-spacing:1px}
.dots{left:576px;top:288px;display:flex;gap:8px}
.dots span{width:13px;height:13px;border-radius:50%;border:2px solid var(--white)}
.dots span.on{background:var(--white)}

/* contact */
.contact-copy{left:94px;top:3608px;width:493px;font-size:14px;line-height:1.65;color:#444}
.contact-copy p{margin-bottom:14px}
.contact-copy a{color:var(--azure);text-decoration:none}
.contact-form{left:613px;top:3608px;width:493px}
.field{display:block;width:493px;height:47px;border:1px solid var(--line);margin-bottom:13px;padding:0 14px;line-height:45px;font-size:14px;color:#9bb}
.field.area{height:228px;line-height:1;padding-top:14px}
.send{display:block;width:80px;height:51px;background:var(--bright);color:var(--white);border:0;font-size:14px;font-weight:600;text-transform:uppercase;margin-top:23px}

/* footer */
.site-footer{left:0;top:4173px;width:1200px;height:185px;background:var(--night)}
.to-top{left:586px;top:40px}
.copyright{left:94px;top:138px;color:#ccc;font-size:12px}
</style>
</head>
<body>

<header class="site-header abs">
  <div class="brand abs"><span class="name">HARBORLINE</span><span class="sub">POOL SERVICE</span></div>
  <ul class="nav abs">
    <li>Home</li>
    <li>About Us</li>
    <li class="active">Services Offered</li>
    <li>FAQ's</li>
    <li>Why Hire Us</li>
    <li>Contact</li>
  </ul>
</header>
<ul class="dropdown abs">
  <li>Residential Pools</li>
  <li class="current">Commercial Pools</li>
</ul>

<section class="hero abs">
  <div class="hero-band abs"></div>
  <div class="hero-band-thin abs"></div>
  <div class="hero-photo abs" role="img" aria-label="Clear blue swimming pool with steel ladder"></div>
  <p class="tagline abs">Water so bright, you'll want to dive right <em>in</em>.</p>
</section>

<h1 class="intro-title abs">Harborline Pool Service is a leading San Diego swimming pool &amp; spa service company for both residential pools and commercial pools</h1>
<div class="intro-photo abs" role="img" aria-label="Child with swim goggles in a pool"></div>
<div class="intro-copy abs">
  <p>If you're looking for the BEST pool cleaning service at an affordable price available in San Diego, we would love the opportunity to prove that Harborline Pool Service is the answer. We are a family-owned company that was built on integrity and a commitment to earn and keep each customer's trust with every service and repair.</p>
  <p>Customer satisfaction is our highest priority, and we are proud to see how many of our wonderful customers leave great <a href="#">reviews</a>.</p>
</div>

<section class="projects abs">
  <h2 class="section-title">Recent Projects</h2>
  <div class="project-grid abs">
    <div class="tile t1" role="img" aria-label="Pool at night"><span class="tile-plus">+</span><span class="tile-label">Lorem Ipsum Dolor</span></div>
    <div class="tile t2" role="img" aria-label="Hotel pool at dusk"></div>
    <div class="tile t3" role="img" aria-label="Indoor pool under glass roof"></div>
    <div class="tile t4" role="img" aria-label="Infinity pool overlooking the sea"></div>
    <div class="tile t5" role="img" aria-label="Lit backyard pool in the evening"></div>
    <div class="tile t6" role="img" aria-label="Indoor pool with wooden walls"></div>
  </div>
</section>

<h2 class="section-title services-title abs">Our Services</h2>
<ul class="service-list col-a abs">
  <li><svg width="22" height="20" viewBox="0 0 22 20"><path d="M2 11 L8 17 L20 2" fill="none" stroke="#0592cd" stroke-width="3.5"/></svg>Swimming Pool and Spa Cleaning</li>
  <li><svg width="22" height="20" viewBox="0 0 22 20"><path d="M2 11 L8 17 L20 2" fill="none" stroke="#0592cd" stroke-width="3.5"/></svg>New Pool and Spa Start Ups</li>
  <li><svg width="22" height="20" viewBox="0 0 22 20"><path d="M2 11 L8 17 L20 2" fill="none" stroke="#0592cd" stroke-width="3.5"/></svg>Troubleshoot and Repair pumps, filters, heaters and heat exchangers</li>
  <li><svg width="22" height="20" viewBox="0 0 22 20"><path d="M2 11 L8 17 L20 2" fill="none" stroke="#0592cd" stroke-width="3.5"/></svg>Tile Cleaning &amp; Restoration</li>
  <li><svg width="22" height="20" viewBox="0 0 22 20"><path d="M2 11 L8 17 L20 2" fill="none" stroke="#0592cd" stroke-width="3.5"/></svg>CPO (Certified Pool Operator) Insured</li>
  <li><svg width="22" height="20" viewBox="0 0 22 20"><path d="M2 11 L8 17 L20 2" fill="none" stroke="#0592cd" stroke-width="3.5"/></svg>Reliable and affordable pool and spa maintenance</li>
  <li><svg width="22" height="20" viewBox="0 0 22 20"><path d="M2 11 L8 17 L20 2" fill="none" stroke="#0592cd" stroke-width="3.5"/></svg>Brushing walls and tile cleaning</li>
  <li><svg width="22" height="20" viewBox="0 0 22 20"><path d="M2 11 L8 17 L20 2" fill="none" stroke="#0592cd" stroke-width="3.5"/></svg>Pool leakage detection and repairs</li>
  <li><svg width="22" height="20" viewBox="0 0 22 20"><path d="M2 11 L8 17 L20 2" fill="none" stroke="#0592cd" stroke-width="3.5"/></svg>Eliminating leaves and debris</li>
  <li><svg width="22" height="20" viewBox="0 0 22 20"><path d="M2 11 L8 17 L20 2" fill="none" stroke="#0592cd" stroke-width="3.5"/></svg>Prompt swimming pool cleaning each week</li>
</ul>
<ul class="service-list col-b abs">
  <li><svg width="22" height="20" viewBox="0 0 22 20"><path d="M2 11 L8 17 L20 2" fill="none" stroke="#0592cd" stroke-width="3.5"/></svg>Install and repair lighting</li>
  <li><svg width="22" height="20" viewBox="0 0 22 20"><path d="M2 11 L8 17 L20 2" fill="none" stroke="#0592cd" stroke-width="3.5"/></svg>Leak Detection Salt System Conversions</li>
  <li><svg width="22" height="20" viewBox="0 0 22 20"><path d="M2 11 L8 17 L20 2" fill="none" stroke="#0592cd" stroke-width="3.5"/></svg>Fountain Cleaning and Service</li>
  <li><svg width="22" height="20" viewBox="0 0 22 20"><path d="M2 11 L8 17 L20 2" fill="none" stroke="#0592cd" stroke-width="3.5"/></svg>Licensed and Bonded Swimming Pool Technicians</li>
  <li><svg width="22" height="20" viewBox="0 0 22 20"><path d="M2 11 L8 17 L20 2" fill="none" stroke="#0592cd" stroke-width="3.5"/></svg>Low Rates for Repairs, Maintenance, Cleaning</li>
  <li><svg width="22" height="20" viewBox="0 0 22 20"><path d="M2 11 L8 17 L20 2" fill="none" stroke="#0592cd" stroke-width="3.5"/></svg>Friendly assistance from the staff</li>
  <li><svg width="22" height="20" viewBox="0 0 22 20"><path d="M2 11 L8 17 L20 2" fill="none" stroke="#0592cd" stroke-width="3.5"/></svg>Salt water system maintenance</li>
  <li><svg width="22" height="20" viewBox="0 0 22 20"><path d="M2 11 L8 17 L20 2" fill="none" stroke="#0592cd" stroke-width="3.5"/></svg>Making your pool and spa crystal clear with balanced chemicals</li>
  <li><svg width="22" height="20" viewBox="0 0 22 20"><path d="M2 11 L8 17 L20 2" fill="none" stroke="#0592cd" stroke-width="3.5"/></svg>Noisy pool motor repairs</li>
  <li><svg width="22" height="20" viewBox="0 0 22 20"><path d="M2 11 L8 17 L20 2" fill="none" stroke="#0592cd" stroke-width="3.5"/></svg>Cleaning out debris in skimmer and pool pump basket</li>
</ul>

<h2 class="section-title areas-title abs">Service Areas</h2>
<ul class="area-list abs">
  <li>Carmel Valley (92130)</li>
  <li>Del Mar (92014)</li>
  <li>Rancho Santa Fe (92067)</li>
  <li>Solana Beach (92075)</li>
  <li>Santaluz (92127)</li>
  <li>Cardiff (92007)</li>
  <li>Encinitas (92024)</li>
  <li>Carlsbad (92009, 92008)</li>
  <li>La Jolla (92037)</li>
  <li>Pacific Beach (92109)</li>
  <li>Mira Mesa (92126)</li>
  <li>Sorrento Valley (92121)</li>
  <li>Clairemont (92117)</li>
  <li>Rancho Bernardo (92127, 92128)</li>
  <li>Rancho Penasquitos (92129)</li>
  <li>Poway (92064)</li>
</ul>

<section class="testimonials abs">
  <h2 class="section-title">What Our Clients Say</h2>
  <p class="quote abs">"Working with Dane is <strong>terrific</strong>. His education and professional background sets him apart from all the other pool cleaners. He has excellent communication with us and he shows up when he says he will. Harborline is the only pool care company I have ever recommended to my friends."</p>
  <p class="cite abs">MARCUS HALE</p>
  <div class="dots abs"><span class="on"></span><span></span></div>
</section>

<div class="contact-copy abs">
  <p>We <strong>guarantee your satisfaction</strong> on each and every service call and repair. Your pool, spa or fountain should be a blessing and not a hassle or a headache. Trust Harborline Pool Service to keep your water sparkling and clear and your equipment in top-notch shape!</p>
  <p>If it's got a pump and a filter we can clean it, repair it, and keep it in top condition! Give us a call at (555) 014-2087, fill out the form to the right, or go to our <a href="#">Contact Us</a> page now.</p>
</div>
<form class="contact-form abs">
  <span class="field">Your Name</span>
  <span class="field">Your Email</span>
  <span class="field">Your Phone Number</span>
  <span class="field area">Your Message</span>
  <button class="send" type="button">Send</button>
</form>

<footer class="site-footer abs">
  <svg class="to-top abs" width="28" height="16" viewBox="0 0 28 16" aria-label="Back to top"><path d="M2 14 L14 3 L26 14" fill="none" stroke="#ffffff" stroke-width="3"/></svg>
  <p class="copyright abs">Copyright © 2015 Harborline Pool Service</p>
</footer>

</body>
</html>
```